Catalog Design for Brisk Meadow

I would like a catalog design for a chicken coop company. We sell chicken coops all over the USA and need a nice catalog to send to our customers. The catalog should be 5.5x8.5 and feature our various collections.

You can see our collections on our website. The catalog should have an index to highlight the various coop collections.

We focus on mobile chicken coops and chicken houses for farmers and homesteaders.

1. Tarrow Forge Mobile Coops (aluminum coops)
https://www.briskmeadow.example/product-category/steel-chicken-coops/
These come in two styles, one for Layers and Broilers
2. HaulNest Mobile Coops (steel coops)
These come in two styles. The HaulNest and The Drifter Coops
https://www.briskmeadow.example/product-category/mobile-coops/
3. Red Dune Coops (free range coops)
https://www.briskmeadow.example/product-category/red-dune-collection/
4. FieldMaxx Chicken Coops
https://www.briskmeadow.example/product-category/mobile-chicken-houses/
5. The Ridgeford Coops (galvanized coops)
https://www.briskmeadow.example/product-category/ridgeford-coops/galvanized-steel-coops/

Our website is https://www.briskmeadow.example/

I would like this delivered as a design concept and then I would consider working with the winner to develop out the design further.

I would like each coop featured on a page showing its features, capacity etc.

There could be an intro page to each collection highlighting the features of that collection etc.

There should also be a page connected to each collection showing options and features available.

I added photos for the Tarrow Forge collection. If you could start with those to give me a design, that would be lovely.

Please let me know if you need more information.

Please note the BrightRoost catalog. They are competitors so we cannot copy it but maybe give an idea for some of what we want.

Use color seems that go with our logo and website.

Target Market(s)

Farmers and homesteaders

Industry/Entity Type

Farming

Font styles to use
Serif

Requirements
Must have
• Nice design, farmer feel

```html
<!DOCTYPE html>
<html lang="en">
<head>
<meta charset="utf-8">
<title>Brisk Meadow Catalog – Front, Inner Spread, Back</title>
<link href="https://fonts.googleapis.com/css2?family=Tinos:wght@400;700&display=swap" rel="stylesheet">
<style>
:root{
  --board:#9c9c9c;
  --red:#c9493b;
  --red-deep:#b23a2d;
  --ink:#2c2c2c;
  --muted:#666;
  --paper:#ffffff;
  --gold:#e9a72a;
}
*{box-sizing:border-box;margin:0;padding:0}
html,body{width:680px;height:1200px;overflow:hidden;background:var(--board);font-family:"Tinos",serif;color:var(--ink)}
.board{position:relative;width:680px;height:1200px}
.caption{position:absolute;color:#fff;font-weight:700;font-size:15px;letter-spacing:.5px}
.photo{position:absolute}
.brand{display:flex;align-items:center;gap:5px;font-weight:700;color:var(--red)}
.brand .dot{width:7px;height:7px;border-radius:50%;background:currentColor}

/* FRONT COVER */
.cover{position:absolute;left:134px;top:70px;width:415px;height:328px;background:var(--paper);overflow:hidden}
.cover .hero{left:0;top:0;width:415px;height:328px;background:linear-gradient(180deg,#f4f4f2 0%,#e6ebe3 22%,#8eae64 42%,#5b8a36 70%,#3f6b27 100%)}
.cover .brand{position:absolute;left:50%;top:26px;transform:translateX(-50%);font-size:12px;background:#fff;padding:4px 12px;border-radius:4px;white-space:nowrap}
.cover .band{position:absolute;left:0;top:0}
.cover .title{position:absolute;left:21px;top:232px;color:#fff;font-weight:700;font-size:16px;line-height:16px}
.cover .lede{position:absolute;left:21px;top:284px;width:206px;color:#fff;font-size:4.4px;line-height:6px}
.cover .url{position:absolute;left:0;top:313px;width:117px;height:11px;background:#fff;border-radius:0 6px 6px 0;color:var(--red);font-size:5.5px;line-height:11px;padding-left:18px}
.cover .disc{position:absolute;width:56px;height:56px;border-radius:50%;border:2px solid #fff}

/* INNER SPREAD */
.spread{position:absolute;left:34px;top:482px;width:618px;height:242px;background:var(--paper)}
.spread .head{position:absolute;left:0;top:0;width:312px;height:15px;background:var(--red);color:#fff;font-weight:400;font-size:9.5px;line-height:15px;text-align:center}
.spread .accent{position:absolute;background:var(--red)}
.spread .panel{position:absolute;left:312px;top:0;width:163px;height:242px;background:var(--red)}
.prod-name{position:absolute;font-weight:700;font-size:8px;color:var(--red);white-space:nowrap}
.price{position:absolute;font-weight:700;font-size:6.5px}
.stars{position:absolute;color:var(--gold);font-size:5px;letter-spacing:.5px}
.copy{position:absolute;font-size:3.6px;line-height:5px;color:var(--muted)}
.note{position:absolute;font-size:3.8px;color:var(--red)}
.bullets{position:absolute;font-size:3.4px;line-height:4.8px;color:var(--muted);list-style:none}
.bullets li::before{content:"▪ ";color:var(--red)}
.thumb{position:absolute;border-radius:5px;border:1.5px solid #fff}

/* BACK COVER */
.back{position:absolute;left:145px;top:800px;width:410px;height:322px;overflow:hidden}
.back .backdrop{left:0;top:0;width:410px;height:322px;background:linear-gradient(135deg,#c9372c 0%,#d84a3c 55%,#e86a5e 100%)}
.back .brand{position:absolute;left:50%;top:150px;transform:translateX(-50%);font-size:14px;color:#fff;padding:6px 16px;white-space:nowrap}
.back .contact-title{position:absolute;left:14px;top:234px;color:#fff;font-weight:700;font-size:9.5px}
.back .contact{position:absolute;left:14px;list-style:none;color:#fff;font-size:6.5px}
.back .contact li{display:flex;align-items:center;gap:5px;height:20px}
.back .contact svg{width:9px;height:9px}
.back .ship-badge{position:absolute;left:176px;top:270px;width:56px;height:20px;background:#fff;border-radius:4px}
.back .social{position:absolute;left:176px;top:300px;display:flex;gap:6px}
.back .social span{width:10px;height:10px;border-radius:2px;background:#fff}
.back .url{position:absolute;right:26px;top:306px;color:#fff;font-size:5.8px}
</style>
</head>
<body>
<main class="board">

  <!-- FRONT COVER -->
  <section class="cover">
    <div class="photo hero" role="img" aria-label="Photo of hens grazing on green pasture in front of a white mobile coop"></div>
    <div class="brand"><span class="dot"></span>Brisk Meadow</div>
    <svg class="band" width="415" height="328" viewBox="0 0 415 328" aria-hidden="true">
      <path d="M0 222 C80 205 200 198 300 245 C350 268 390 265 415 255 L415 328 L0 328 Z" fill="var(--red)"/>
      <path d="M0 222 C80 205 200 198 300 245 C350 268 390 265 415 255" fill="none" stroke="#fff" stroke-width="1.5"/>
    </svg>
    <h1 class="title">Commercial<br>Mobile Coops &amp;<br>Backyard Coops</h1>
    <p class="lede">Give your flock a better home with a mobile coop from Brisk Meadow. We are your source for commercial mobile coops and backyard chicken coops built in the USA. Your chickens, ducks and turkeys will thrive, and your family and customers will enjoy better food.</p>
    <div class="url"><b>www.briskmeadow.example</b></div>
    <div class="disc" role="img" aria-label="Open-sided coop with hens" style="left:236px;top:256px;background:linear-gradient(180deg,#a9c6e0,#6c8a4c)"></div>
    <div class="disc" role="img" aria-label="Coop on a farm" style="left:295px;top:260px;background:linear-gradient(180deg,#c8d9ea,#8a6b4a)"></div>
    <div class="disc" role="img" aria-label="Row of coops on pasture" style="left:354px;top:255px;background:linear-gradient(180deg,#9fc1e3,#7aa05a)"></div>
  </section>
  <p class="caption" style="left:301px;top:418px">FRONT</p>

  <!-- INNER SPREAD -->
  <section class="spread">
    <h2 class="head">Aluminum Mobile Coops For Sale in Harlow AR</h2>

    <div class="accent" style="left:8px;top:24px;width:20px;height:38px"></div>
    <div class="photo" role="img" aria-label="10×18 white mobile coop on grass under trees" style="left:14px;top:28px;width:148px;height:100px;background:linear-gradient(180deg,#9cc2e6 0%,#d9e6ee 45%,#6f9143 70%,#4d7130 100%)"></div>
    <h3 class="prod-name" style="left:166px;top:36px">10×18 Mobile Coop</h3>
    <p class="price" style="left:166px;top:50px">$4,680.00</p>
    <p class="stars" style="left:266px;top:47px">★★★★★</p>
    <p class="copy" style="left:166px;top:62px;width:132px">The 10×18 mobile coop houses up to 90 laying hens or 100 broilers. It has four easy-to-move wheels, a walk-in door, durable canvas and a roosting bar. One person can move it with ease, and the roomy shelter keeps birds safe.</p>
    <p class="copy" style="left:166px;top:92px;width:132px">Recommended with a 16 gallon water tank, 2 waterers and 2 feeders.</p>
    <p class="note" style="left:166px;top:108px">FREE Nationwide Shipping in the Lower 48 states.</p>

    <h3 class="prod-name" style="left:12px;top:142px">9×16 Broiler Coops for 100 Chickens</h3>
    <p class="price" style="left:12px;top:156px">$3,715.00</p>
    <p class="stars" style="left:118px;top:154px">★★★★★</p>
    <p class="copy" style="left:12px;top:167px;width:148px">Our 9×16 broiler coop comes with these features and fits up to 100 chickens. It has two wheels for easy moving, two feeders and one waterer.</p>
    <ul class="bullets" style="left:12px;top:182px">
      <li>36 inch Entry Door</li><li>Heavy Duty Tarp</li><li>Front Mount Handle</li><li>Wheels for easy moving</li>
    </ul>
    <ul class="bullets" style="left:86px;top:182px">
      <li>2 aluminum feeders</li><li>2 bell waterers</li><li>16 gallon water tank</li><li>4 ft tall at the peak</li>
    </ul>
    <p class="copy" style="left:12px;top:206px">Maximize the productivity of your broilers with this coop.</p>
    <p class="note" style="left:12px;top:216px">Maximize the FREE Nationwide Shipping in the Lower 48</p>
    <div class="accent" style="left:282px;top:130px;width:24px;height:30px"></div>
    <div class="photo" role="img" aria-label="Low white broiler coop beside a cornfield" style="left:166px;top:136px;width:134px;height:100px;background:linear-gradient(180deg,#7c9c4c 0%,#5c8532 35%,#e8ebe6 55%,#7a9a46 80%,#4e7230 100%)"></div>

    <div class="panel"></div>
    <div class="photo" role="img" aria-label="Winter enclosure coop on open pasture" style="left:326px;top:10px;width:144px;height:104px;background:linear-gradient(180deg,#5f8fcf 0%,#a9c9ea 45%,#e8e8e4 65%,#7c8f3e 85%,#5e7a2e 100%)"></div>
    <h3 class="prod-name" style="left:326px;top:122px;color:#fff">Winter Enclosures For HaulNest</h3>
    <p class="price" style="left:326px;top:136px;color:#fff">$4,680.00</p>
    <p class="stars" style="left:430px;top:134px;color:#fff">★★★★★</p>
    <p class="copy" style="left:326px;top:148px;width:140px;color:#fff">It is important to keep your chickens warm in the colder months, and we have the right enclosures for you.</p>
    <p class="copy" style="left:326px;top:161px;width:140px;color:#fff">These winter enclosures keep birds safe, warm and healthy, shielding them from cold temperatures, wind, snow and predators.</p>
    <h4 class="prod-name" style="left:326px;top:182px;color:#fff;font-size:7px">Related products</h4>
    <div class="thumb" role="img" aria-label="Small coop enclosure" style="left:326px;top:194px;width:80px;height:42px;background:linear-gradient(135deg,#d7d9d6,#8d8f88)"></div>
    <div class="thumb" role="img" aria-label="Coops on a farm" style="left:410px;top:194px;width:60px;height:42px;background:linear-gradient(180deg,#b9d0e6,#7a8a55)"></div>

    <h3 class="prod-name" style="left:481px;top:10px;color:var(--ink)">10×12 Drifter HaulNest</h3>
    <p class="price" style="left:481px;top:26px">$2,705.00</p>
    <p class="stars" style="left:575px;top:24px;color:#ccc">★★★★★</p>
    <p class="copy" style="left:481px;top:40px;width:130px">The 10×12 Drifter HaulNest is made of tough steel that is powder coated. It holds up to 60 laying hens or 80 broilers. It has two wheels lifted by a handle, a large entry door, durable canvas and a roosting bar. The roof is not made for heavy snow.</p>
    <p class="note" style="left:481px;top:74px;font-weight:700">FREE Nationwide Shipping in the Lower 48 states.</p>
    <h3 class="prod-name" style="left:481px;top:84px;color:var(--ink)">10×12 Drifter Economy Coop</h3>
    <ul class="bullets" style="left:481px;top:98px">
      <li>Large Entry Door</li><li>Simple 1 Step Moving</li><li>Roof and back side tarp</li><li>Welded Fencing Frame</li><li>UV Resistant Tarp</li>
    </ul>
    <ul class="bullets" style="left:560px;top:98px">
      <li>Flat Free Wheels</li><li>Stainless Fasteners</li><li>Powder Coated</li><li>Easy to Assemble</li><li>Roost Bar</li>
    </ul>
    <p class="copy" style="left:481px;top:124px;width:130px">The 10×12 Drifter Mobile Coops answer customers who wanted a more affordable coop. It is good for chickens, ducks or turkeys.</p>
    <div class="photo" role="img" aria-label="Open-frame steel mobile coop on a dry field" style="left:475px;top:160px;width:143px;height:82px;background:linear-gradient(180deg,#e6e8ea 0%,#c7c9c6 30%,#a89a5a 60%,#8a7a3e 100%)"></div>
  </section>
  <p class="caption" style="left:130px;top:743px">INNER_01</p>
  <p class="caption" style="left:483px;top:743px">INNER_02</p>

  <!-- BACK COVER -->
  <section class="back">
    <div class="photo backdrop" role="img" aria-label="Red-toned photo of a mobile coop frame under a tree"></div>
    <div class="brand"><span class="dot"></span>Brisk Meadow</div>
    <svg style="position:absolute;left:0;top:0" width="410" height="322" viewBox="0 0 410 322" aria-hidden="true">
      <path d="M0 215 C90 185 200 205 280 240 C330 262 380 262 410 250 L410 322 L0 322 Z" fill="var(--red-deep)" opacity=".5"/>
      <path d="M0 215 C90 185 200 205 280 240 C330 262 380 262 410 250" fill="none" stroke="#fff" stroke-width="1.5"/>
    </svg>
    <h2 class="contact-title">Contact us</h2>
    <ul class="contact" style="top:250px">
      <li><svg viewBox="0 0 10 10"><path d="M5 0.5a3.3 3.3 0 0 0-3.3 3.3C1.7 6.3 5 9.5 5 9.5s3.3-3.2 3.3-5.7A3.3 3.3 0 0 0 5 .5z" fill="#fff"/><circle cx="5" cy="3.8" r="1.2" fill="var(--red)"/></svg>48 Hollow Creek Road, Dalton, PA 17000</li>
      <li><svg viewBox="0 0 10 10"><circle cx="5" cy="5" r="4.5" fill="#fff"/><path d="M3.4 2.8l1 1-.5.6a3.5 3.5 0 0 0 1.7 1.7l.6-.5 1 1-.6.8c-1.8-.1-3.9-2.2-4-4z" fill="var(--red)"/></svg>(555) 014-2290</li>
      <li><svg viewBox="0 0 10 10"><circle cx="5" cy="5" r="4.5" fill="#fff"/><rect x="2.6" y="3.3" width="4.8" height="3.4" fill="none" stroke="var(--red)" stroke-width=".7"/><path d="M2.6 3.3L5 5.2l2.4-1.9" fill="none" stroke="var(--red)" stroke-width=".7"/></svg>orders@briskmeadow.example</li>
    </ul>
    <div class="ship-badge" role="img" aria-label="Free shipping badge"></div>
    <div class="social" aria-label="Social media links"><span></span><span></span><span></span><span></span></div>
    <div class="photo" role="img" aria-label="Coop with hens, in a circle" style="left:292px;top:232px;width:58px;height:58px;border-radius:50%;border:2px solid #fff;background:linear-gradient(180deg,#b9d3ea,#6e8f4a)"></div>
    <div class="photo" role="img" aria-label="Coop with goats, in a circle" style="left:352px;top:228px;width:58px;height:58px;border-radius:50%;border:2px solid #fff;background:linear-gradient(180deg,#dfe4e6,#8a9a6a)"></div>
    <p class="url">www.briskmeadow.example</p>
  </section>
  <p class="caption" style="left:317px;top:1146px">BACK</p>

</main>
</body>
</html>
```